Lone Star Wetland Flora Stewardship Guild

We need to design the home page of this new website. We would like a fun website design for provides as a resource for members and information for potential members.
Please design so that we can see a portion of background on each side on the website.
I just need the final design files psd no coding needed.
Attached is their logo (colors are not 100% set in stone either so can mess with those as I did in the quick mockup attached)
Attached is a pdf newsletter they send out, you can get a feel for them and what they are about. The design is crappy and we are here to fix that going forward and we are starting with the website.
Here are some quick example websites (design style is open)
- I attached a quick mockup i did just for a content visual but by all means do what you want.
- http://www.brindlecourtleaders.org/
- http://www.qvelto.org/
- http://preview.plimworks7.com/view.php?cat=layoutpacks&host=gridcrafthub&temp=venrolite
- http://www.ploughvale.org/
- http://www.townmarrow.org/
- http://www.projectkindlecoat.org/
here are some of the other chapters website (pretty bad!)
and here are some of the others:
- http://www.zrelkq.org/
- http://ovtu.org/
- http://www.lirvx.org/
Content Items that need to be included:
1. Logo
2. Menu - home, about, members, resources, events, membership, contact
3. Become a member - button or action
4. social links - friendwall, jobrungo, clipzora
5. banner - that needs to explain their purpose "Promoting environmental stewardship through operations, research, education and outreach" (or this can be worked into the design)
6. Upcoming event (s)
7. Advertisement - members can place an ad on the website, this can be a placeholder for now
8. newsletter signup
9. advertise with us - this link can be in the footer
30-60 years of age, succesfull (household budgets of 120K+ men and women that live in texas.
Education

```html
<!DOCTYPE html>
<html lang="en">
<head>
<meta charset="utf-8">
<title>Lone Star Wetland Flora Stewardship Guild</title>
<link href="https://fonts.googleapis.com/css2?family=Arimo:wght@400;700&family=Josefin+Sans:wght@400;600&family=Open+Sans:ital,wght@0,400;0,600;1,400&family=Questrial&family=Merriweather&family=Source+Sans+3:wght@400;600&display=swap" rel="stylesheet">
<style>
:root{
  --red:#d5475a;
  --red-dark:#c23a4c;
  --navy:#103f8a;
  --orange:#f7a21b;
  --ink:#222;
  --grey:#555;
  --muted:#8a8a8a;
  --green:#3d6a2e;
  --footer:#333;
  --panel:#efefef;
}
*{box-sizing:border-box;margin:0;padding:0}
html,body{width:1029px;height:1200px;overflow:hidden}
body{position:relative;font-family:"Arimo",Arial,sans-serif;color:var(--ink);background:#fff}
.abs{position:absolute}
.backdrop{left:0;top:0;width:1029px;height:470px;background:linear-gradient(180deg,#9ec6ea 0%,#dbeaf6 45%,#b9c9a8 75%,#ffffff 100%)}
.page{left:83px;top:470px;width:860px;height:568px;background:#fff}
.brand{left:90px;top:28px;display:flex;align-items:center;gap:8px;width:200px}
.brand-dot{width:26px;height:26px;border-radius:50%;background:var(--navy);flex:none}
.brand-name{font-family:"Josefin Sans",sans-serif;font-weight:600;font-size:15px;line-height:18px;color:var(--red)}
.account{left:430px;top:44px;font-family:"Open Sans",sans-serif;font-size:17px;color:#444}
.phone{left:584px;top:44px;display:flex;align-items:center;gap:7px;color:#555;font-family:"Open Sans",sans-serif}
.phone small{font-size:14px}
.phone b{font-weight:400;font-size:23px}
.nav{left:292px;top:96px;width:651px;height:37px}
.nav-links{left:309px;top:96px;height:37px;display:flex;align-items:center;list-style:none;font-family:"Arimo",sans-serif;font-size:11px;color:#fff}
.nav-links li{padding:0 18px;border-left:1px solid #2b5aa3;line-height:26px}
.nav-links li:first-child{border:0;background:var(--red);padding:0 14px}
.hero-photo{left:86px;top:135px;width:546px;height:312px;background:linear-gradient(160deg,#6d8c7a 0%,#3d5a3f 40%,#78a64c 65%,#243321 100%)}
.hero-panel{left:632px;top:135px;width:311px;height:312px;background:var(--red)}
.cta{left:647px;width:282px;height:40px;background:#fff;display:flex;align-items:center}
.cta-icon{width:42px;height:40px;background:linear-gradient(#fbb93a,var(--orange));display:flex;align-items:center;justify-content:center}
.cta span{padding-left:22px;font-family:"Josefin Sans",sans-serif;font-size:18px;letter-spacing:1.5px;color:#888}
.stay{left:649px;top:349px;font-family:"Josefin Sans",sans-serif;font-weight:600;font-size:17px;color:#fff;letter-spacing:.5px}
.social-box{left:653px;top:379px;width:241px;height:51px;border:2px solid #fff;display:grid;grid-template-columns:1fr 1fr;align-content:center;padding:0 22px;row-gap:3px}
.social-box span,.foot-social span{display:flex;align-items:center;gap:5px;font-size:11px;color:#fff}
.social-box i,.foot-social i{width:9px;height:9px;border-radius:50%;background:#fff;display:block}
.welcome{left:86px;top:468px;font-family:"Questrial",sans-serif;font-size:27px;color:var(--red)}
.welcome-sub{left:86px;top:497px;font-family:"Questrial",sans-serif;font-size:20px;letter-spacing:1.2px;color:#111;white-space:nowrap}
.rule-dash{left:86px;top:525px;width:564px;border-top:1px dashed #bbb}
.intro{left:90px;top:534px;width:560px;font-size:10.5px;line-height:17px;color:#111}
.intro p{margin-bottom:16px}
.ticks{list-style:none;margin-top:-6px}
.ticks li{display:flex;align-items:center;gap:5px;line-height:19px}
.news{left:692px;top:480px;width:250px;height:233px;background:var(--panel);border:1px solid #d8d8d8;border-radius:4px}
.news h3{position:absolute;left:12px;top:10px;font-family:"Open Sans",sans-serif;font-weight:600;font-size:22px;color:#333}
.news h3 em{font-style:normal;color:var(--red)}
.news label{position:absolute;left:23px;font-size:11px;color:#777}
.news .field{position:absolute;left:22px;width:189px;height:32px;background:#fff;border:1px solid #ccc;border-radius:3px}
.subscribe{position:absolute;left:111px;top:192px;width:112px;height:30px;border-radius:4px;background:linear-gradient(#9a9a9a,#6d6d6d);border:1px solid #555;color:#fff;font-family:"Source Sans 3",sans-serif;font-size:16px;text-align:center;line-height:28px}
.divider{left:83px;top:753px;width:845px;border-top:1px solid #e2e2e2}
.vline{top:793px;height:227px;border-left:1px solid #ddd}
.col-title{top:784px;font-family:"Source Sans 3",sans-serif;font-size:18px;color:#444}
.col-title em{font-style:normal;color:var(--green)}
.event{left:86px;width:260px;display:flex;gap:14px}
.date{width:79px;height:51px;flex:none}
.event p{font-size:10.5px;line-height:14px;color:#444}
.dotted{left:87px;top:885px;width:259px;border-top:1px dotted #999}
.view-all{left:289px;top:958px;font-size:10.5px;font-weight:700;color:#234}
.ad-art{left:415px;top:813px;width:250px;height:109px;background:linear-gradient(180deg,#e7e6e2 0%,#d8d4c6 70%,#b9a780 100%)}
.ad-copy{left:414px;top:934px;width:265px;font-size:10.5px;line-height:16px;color:#444}
.quote{left:731px;top:825px;width:214px;font-size:10.5px;line-height:15.5px;color:#444}
.quote b{font-family:Georgia,serif;font-size:18px;color:#555;font-weight:400}
.byline{left:760px;top:940px;width:124px;text-align:right;font-family:"Open Sans",sans-serif;font-size:9.5px;line-height:17px}
.byline em{color:#b22}
.byline span{font-style:italic}
.avatar{left:897px;top:932px;width:45px;height:39px;background:linear-gradient(#c9a27a,#8c6540);border:2px solid #fff;box-shadow:0 0 2px #999}
.footer{left:0;top:1038px;width:1029px;height:162px;background:var(--footer)}
.advertise{left:353px;top:1056px;width:306px;height:36px;border-radius:4px;background:#555;border:1px solid #777;overflow:hidden}
.advertise span{position:absolute;left:26px;top:8px;font-family:"Source Sans 3",sans-serif;font-weight:600;font-size:17px;color:#ddd;letter-spacing:.5px}
.advertise a{position:absolute;right:0;top:0;width:72px;height:36px;background:var(--red);color:#fff;font-size:8px;font-weight:700;text-decoration:underline;text-align:center;line-height:36px}
.foot-rule{left:123px;top:1106px;width:779px;border-top:2px solid #111}
.foot-brand{left:129px;top:1128px;display:flex;align-items:center;gap:6px;width:125px}
.foot-brand i{width:16px;height:16px;border-radius:50%;background:#999;flex:none}
.foot-brand span{font-family:"Josefin Sans",sans-serif;font-weight:600;font-size:11px;line-height:13px;color:#bbb}
.foot-nav{left:279px;top:1140px;display:flex;list-style:none;font-size:11px;color:#fff}
.foot-nav li+li::before{content:"|";padding:0 9px}
.foot-social{left:812px;top:1130px;display:grid;grid-template-columns:auto auto;gap:4px 10px}
.copy{left:0;top:1174px;width:1029px;text-align:center;font-size:10.5px;color:#aaa}
</style>
</head>
<body>
<div class="abs backdrop" role="img" aria-label="Soft sky and lakeside tree line behind the page"></div>

<header>
  <div class="abs brand"><span class="brand-dot"></span><span class="brand-name">Lone Star Wetland Flora Stewardship Guild</span></div>
  <div class="abs account">Login &nbsp;/&nbsp; Register</div>
  <div class="abs phone">
    <svg width="22" height="22" viewBox="0 0 24 24"><path fill="#555" d="M6.6 10.8a15 15 0 0 0 6.6 6.6l2.2-2.2c.3-.3.7-.4 1-.2 1.1.4 2.3.6 3.6.6.6 0 1 .4 1 1V20c0 .6-.4 1-1 1A17 17 0 0 1 3 4c0-.6.4-1 1-1h3.5c.6 0 1 .4 1 1 0 1.3.2 2.5.6 3.6.1.3 0 .7-.2 1z"/></svg>
    <small>Contact Us Today:</small> <b>+44 (0)1555 01473</b>
  </div>
  <svg class="abs nav" viewBox="0 0 651 37"><polygon points="18,0 651,0 651,37 0,37" fill="#103f8a"/></svg>
  <ul class="abs nav-links">
    <li>HOME</li><li>ABOUT</li><li>MEMBERS</li><li>RESOURCES</li><li>EVENTS</li><li>MEMBERSHIP</li><li>CONTACT</li>
  </ul>
</header>

<section>
  <div class="abs hero-photo" role="img" aria-label="Water lily blooming among lily pads and reeds on a still pond"></div>
  <div class="abs hero-panel"></div>
  <div class="abs cta" style="top:193px"><div class="cta-icon"><svg width="18" height="22" viewBox="0 0 18 22"><circle cx="9" cy="6" r="5" fill="#1d3f78"/><rect x="1" y="12" width="16" height="10" rx="4" fill="#1d3f78"/></svg></div><span>BECOME A MEMBER</span></div>
  <div class="abs cta" style="top:240px"><div class="cta-icon"><svg width="14" height="22"><text x="1" y="18" font-family="Arimo" font-weight="700" font-size="20" fill="#1d3f78">$</text></svg></div><span>DONATE NOW</span></div>
  <div class="abs cta" style="top:286px"><div class="cta-icon"><svg width="20" height="22" viewBox="0 0 20 22"><circle cx="8" cy="8" r="6" fill="none" stroke="#1d3f78" stroke-width="3"/><line x1="12" y1="13" x2="18" y2="20" stroke="#1d3f78" stroke-width="3"/></svg></div><span>FIND YOUR LOCAL UNIT</span></div>
  <div class="abs stay">Stay Connected :</div>
  <div class="abs social-box"><span><i></i>friendwall</span><span><i></i>clipzora</span><span><i></i>chirpline</span><span><i></i>feed</span></div>
</section>

<div class="abs page"></div>
<main>
  <h1 class="abs welcome">WELCOME TO</h1>
  <h2 class="abs welcome-sub">Lone Star Wetland Flora Stewardship Guild</h2>
  <div class="abs rule-dash"></div>
  <div class="abs intro">
    <p>The Civic Carry Defense League is a project started in 2008 by Dorian Velk, founder of holsterfree.org. Living "behind enemy lines" in Illinois and trying to promote the right to carry a firearm for defense, Dorian found himself arrested and having to face charges such as "disorderly conduct" for wearing an empty holster, and "aggravated unlawful use of a weapon" (class 4 felony) for carrying a pistol, unloaded and in a container exactly as prescribed by law.</p>
    <p>It was clear that adherence to common-sense and even the system known as law had been abandoned by police, lawyers, judges, and journalists. And this was clear all over the country.</p>
    <ul class="ticks">
      <li><svg width="13" height="11" viewBox="0 0 13 11"><path d="M1 6l4 4 7-9" fill="none" stroke="#3d6a2e" stroke-width="2.5"/></svg>Criminal/Civil Legal Costs from a Self-Defense Situation --&gt; You Have Support!</li>
      <li><svg width="13" height="11" viewBox="0 0 13 11"><path d="M1 6l4 4 7-9" fill="none" stroke="#3d6a2e" stroke-width="2.5"/></svg>Unlawful Detainment, Arrest, Charges, and Other Harassment --&gt; You Have Support!</li>
    </ul>
  </div>

  <aside class="abs news">
    <h3>Newsletter <em>Signup</em></h3>
    <label style="top:67px">Name</label><div class="field" style="top:88px"></div>
    <label style="top:130px">Email</label><div class="field" style="top:150px"></div>
    <div class="subscribe">Subscribe</div>
  </aside>

  <div class="abs divider"></div>
  <div class="abs vline" style="left:383px"></div>
  <div class="abs vline" style="left:701px"></div>

  <h3 class="abs col-title" style="left:86px">Upcoming <em>Events</em></h3>
  <div class="abs event" style="top:817px">
    <svg class="date" viewBox="0 0 79 51"><polygon points="0,0 68,0 79,25 68,51 0,51" fill="#d5475a"/><text x="32" y="21" text-anchor="middle" font-family="Merriweather" font-size="17" fill="#fff">31</text><text x="34" y="42" text-anchor="middle" font-family="Merriweather" font-size="17" fill="#fff">July</text></svg>
    <p>simply dummy text of the printing and typesetting industry. Lorem Ipsum has been the simply dummy text of the printing and typesetting industry.</p>
  </div>
  <div class="abs dotted"></div>
  <div class="abs event" style="top:902px">
    <svg class="date" viewBox="0 0 79 51"><polygon points="0,0 68,0 79,25 68,51 0,51" fill="#d5475a"/><text x="32" y="21" text-anchor="middle" font-family="Merriweather" font-size="17" fill="#fff">31</text><text x="34" y="42" text-anchor="middle" font-family="Merriweather" font-size="17" fill="#fff">July</text></svg>
    <p>simply dummy text of the printing and typesetting industry. Lorem Ipsum has been the simply dummy text of the printing and typesetting industry.</p>
  </div>
  <div class="abs view-all">View All...</div>

  <h3 class="abs col-title" style="left:413px">Post <em>Advertisement</em></h3>
  <div class="abs ad-art" role="img" aria-label="Member advertisement artwork: hand-lettered message about the environment above a lone tree on a hill"></div>
  <p class="abs ad-copy">simply dummy text of the printing and typesetting indu-stry. Lorem Ipsum has been the simply dummy text of the printing.</p>

  <h3 class="abs col-title" style="left:728px;top:788px;font-size:20px">Clients <em>Testimonial</em></h3>
  <p class="abs quote"><b>&ldquo;</b> simply dummy text of the printing and typesetting industry. Lorem Ipsum has been the simply dummy text of the printing and typesetting industry. Lorem Ipsum has been the simply dummy Ipsum has been the simply dummy text of text . <b>&rdquo;</b></p>
  <div class="abs byline"><em>By Dara Quillen</em><br><span>Posted on Nov25, 2013</span></div>
  <div class="abs avatar" role="img" aria-label="Portrait photo of the reviewer"></div>
</main>

<footer>
  <div class="abs footer"></div>
  <div class="abs advertise"><span>ADVERTISE WITH US</span><a>Click Here</a></div>
  <div class="abs foot-rule"></div>
  <div class="abs foot-brand"><i></i><span>Lone Star Wetland Flora Stewardship Guild</span></div>
  <ul class="abs foot-nav"><li>HOME</li><li>ABOUT</li><li>MEMBERS</li><li>RESOURCES</li><li>EVENTS</li><li>MEMBERSHIP</li><li>CONTACT</li></ul>
  <div class="abs foot-social"><span><i></i>friendwall</span><span><i></i>chirpline</span><span><i></i>jobrungo</span><span><i></i>circlo</span></div>
  <p class="abs copy">Copyright © 2014 Lswfsg. All Rights Reserved</p>
</footer>
</body>
</html>
```